Wine Shop Banners

Banner graphic/images required
Require banner images to match the present online wine shop.

www.kelterhaus-traube.de

The wine-shop presently has a very clean, simple design, lots of white space, which is very much the trend at the moment.

Requirements
Images or graphic design for present banners visible on the homepage

The colour and feeling of the banners must fit in with the present clean, simple design.

Work required
3 large slide-card/banners (can be more) and 3 smaller fixed banners below. Please view website to see present position of banners.

LARGE BANNERS x 3

Something special with white background within the banner space
White background on each slide-card. Small individual graphic image in the middle of the slide card. This could be either a simple element of wine:
ingredients, fruit (grape), bottle, cork, old bottle label etc. just displaying one item on each slide-card. Preferably with high quality graphic features.

Note:
We are trying the steer away from the classic stereotype wineshop design. The image/s should have a higher, individual graphic touch, which gives the design something different. Sometimes such artistic work is displayed in steampunk or even in nostalgic design, which leaves the viewer slightly memorized with the content.
To clarify: we are not looking for a full steampunk design but possibly certain elements of this will give you an idea what we mean. That is to say, the design can go slightly in this direction without going over the top. Something small but very eye-catching.

SMALLER BANNERS x 3

One idea is:
Showing a symbol e.g. - discount sign "%" against a white background but again with a high graphic quality.

Target Market(s)

People interested in purchasing wine.
Ages approx. 25 to 65

Industry/Entity Type

Shop

Requirements
Must have
• Something special with white background
• Small individual graphic image in the middle of the slide card.
Nice to have
• The image/s should have a higher, individual graphic touch, which gives the design something different. Something that leaves the viewer slightly memorized with the content.
Should not have
• Not the typical classical design that is often seen on wine shops.

```html
<!DOCTYPE html>
<html lang="de">
<head>
<meta charset="utf-8">
<title>Kelterhaus Traube – Wein Shop</title>
<link rel="stylesheet" href="https://fonts.googleapis.com/css2?family=Cabin:wght@400;500&family=Kreon:wght@400&family=Crimson+Text&display=swap">
<style>
:root{
  --wine:#a8224a;
  --olive:#5a6130;
  --lime:#d3dd5f;
  --lime-text:#c6d160;
  --text:#333;
  --ink:#3b2a24;
  --muted:#888;
  --line:#e6e6e6;
  --bg:#fff;
}
*{box-sizing:border-box;margin:0;padding:0}
html,body{width:1200px;height:906px;overflow:hidden;background:var(--bg)}
body{position:relative;font-family:"Cabin",sans-serif;color:var(--text);border-top:1px solid #ccc}
.abs{position:absolute}

.brand{left:75px;top:24px;width:160px;text-align:center;color:var(--olive)}
.brand-name{font-family:"Kreon",serif;font-size:31px;letter-spacing:1px;line-height:38px}
.brand-sub{font-size:13px;letter-spacing:6px;margin-top:4px}

.search{left:588px;top:37px;width:289px;height:32px;border:1px solid #555;display:flex;align-items:center}
.search svg{margin:0 10px}
.search span{flex:1;font-size:14px;color:#666}
.search button{width:42px;height:30px;background:var(--wine);color:#fff;border:0;font:500 15px "Cabin",sans-serif}

.account{left:990px;top:26px;display:flex;align-items:center;gap:12px;font-size:17px;color:#555}

.nav{left:92px;top:116px;display:flex;font-size:17.5px;color:#444}
.nav span{margin-right:36px}
.icons{left:1008px;top:103px;display:flex;gap:20px}
.badge-wrap{position:relative;width:34px;height:34px}
.badge{position:absolute;right:-10px;top:-2px;width:19px;height:19px;border-radius:50%;background:#b7b722;color:#fff;font-size:11px;text-align:center;line-height:19px}

.side{left:75px;top:155px;width:214px}
.side-head{background:var(--lime);height:36px;line-height:36px;padding-left:12px;font-weight:500;font-size:15px;color:#444}
.facet-title{position:absolute;left:0;color:var(--lime-text);font-size:16px}
.facet{position:absolute;left:0;list-style:none;font-size:15px;color:#444}
.facet li{height:23px}
.facet li::before{content:"›";margin-right:7px}
.facet em{font-style:normal;color:var(--muted)}
.scrolltrack{position:absolute;left:195px;top:78px;width:15px;height:165px;background:#f1f1f1}
.scrolltrack i{position:absolute;left:2px;top:17px;width:11px;height:65px;background:#c1c1c1}
.country{height:165px;overflow:hidden}
.slider{position:absolute;left:6px;top:622px;width:193px;height:3px;border:1px solid #999}
.slider::before,.slider::after{content:"";position:absolute;top:-6px;width:9px;height:12px;border:1px solid #999;border-radius:3px;background:#fff}
.slider::before{left:-5px}.slider::after{right:-5px}
.price{position:absolute;left:0;width:214px;top:636px;text-align:center;font-size:13px}
.region{position:absolute;left:2px;top:707px;width:209px;height:38px;border:1px solid #ccc;padding-left:11px;line-height:36px;font-size:14px;color:#666}

.hero{left:300px;top:155px;width:798px;height:311px;background:#fff;border:1px solid var(--line)}
.hero-graphic{position:absolute;left:329px;top:26px;width:140px;height:140px;border-radius:50%;background:radial-gradient(circle at 40% 35%,#c7a27a,#7a3a2e 60%,#4a2420)}
.hero-title{position:absolute;left:19px;top:178px;font-family:"Kreon",serif;font-size:40px;color:var(--ink)}
.hero-btn{position:absolute;left:24px;top:244px;width:130px;height:43px;background:var(--wine);color:#fff;font-family:"Kreon",serif;font-size:21px;text-align:center;line-height:43px}

.promo{top:477px;height:121px;background:linear-gradient(135deg,#f7f3ef,#ece6e0);font-family:"Crimson Text",serif;color:var(--wine);text-align:center;overflow:hidden}
.promo-ship{left:300px;width:258px;font-size:22px;line-height:28px}
.promo-ship p{position:absolute;left:14px;top:18px;width:154px;text-align:center;color:#fff;text-shadow:1px 1px 2px #777}
.promo-ship .star{position:absolute;left:180px;top:38px;width:92px;height:92px;border-radius:50%;background:var(--wine);color:#fff;font-size:32px;line-height:92px;text-align:center;padding-right:14px}
.promo-ann{left:568px;width:259px;font-size:19px;line-height:24px;padding-top:26px;background:linear-gradient(135deg,#fbf3f4,#f3e4e6)}
.promo-spec{left:838px;width:258px;font-size:27px;line-height:31px;padding:28px 60px 0 0}
.promo-spec b{position:absolute;right:6px;bottom:18px;font-weight:400;font-size:22px;color:#b8c13c;transform:rotate(-45deg);line-height:20px}

.section{left:300px;top:620px;display:flex;align-items:center;gap:10px;font-family:"Crimson Text",serif;font-size:17px;color:#222}
.section-line{left:300px;top:646px;width:798px;height:3px;background:var(--line)}
.pager{left:1056px;top:619px;display:flex;gap:4px}
.pager span{width:17px;height:19px;border:1px solid #333;display:flex;align-items:center;justify-content:center}

.card{top:652px;width:198px;height:254px;border:1px solid var(--line);border-bottom:0;text-align:center}
.bottle{position:absolute;top:15px;left:50%;transform:translateX(-50%);width:40px;height:183px;border-radius:14px 14px 6px 6px}
.card p{position:absolute;top:211px;left:8px;right:8px;font-size:14px;line-height:16px;color:#444}
</style>
</head>
<body>

<header>
  <div class="abs brand">
    <div class="brand-name">KELTERHAUS</div>
    <div class="brand-sub">TRAUBE</div>
  </div>

  <div class="abs search">
    <svg width="13" height="13" viewBox="0 0 13 13"><circle cx="5.5" cy="5.5" r="4" fill="none" stroke="#a8224a" stroke-width="2"/><path d="M8.5 8.5l3.5 3.5" stroke="#a8224a" stroke-width="2"/></svg>
    <span>Suche</span>
    <button>GO</button>
  </div>

  <div class="abs account">
    <span>Sign out</span>
    <svg width="26" height="28" viewBox="0 0 26 28" fill="none" stroke="#555" stroke-width="2"><circle cx="13" cy="8" r="6"/><path d="M2 27v-4a6 6 0 0 1 6-6h10a6 6 0 0 1 6 6v4z"/></svg>
  </div>

  <nav class="abs nav">
    <span>red wine</span><span>White wine</span><span>rose wine</span><span>Champagne / champagne</span><span>Special offers</span><span>Tasting packages</span>
  </nav>

  <div class="abs icons">
    <div class="badge-wrap">
      <svg width="34" height="34" viewBox="0 0 34 34" fill="none" stroke="#555" stroke-width="2"><path d="M2 8h5l4 16h16l3-11H9"/><circle cx="13" cy="29" r="2"/><circle cx="25" cy="29" r="2"/></svg>
      <span class="badge">0</span>
    </div>
    <div class="badge-wrap">
      <svg width="34" height="34" viewBox="0 0 34 34"><circle cx="17" cy="17" r="15" fill="#888"/><path d="M17 24l-6-6a3.5 3.5 0 0 1 6-4a3.5 3.5 0 0 1 6 4z" fill="none" stroke="#fff" stroke-width="1.6"/></svg>
      <span class="badge">0</span>
    </div>
  </div>
</header>

<aside class="abs side">
  <div class="side-head">DETAILS SEARCH</div>
  <div class="facet-title" style="top:47px">COUNTRY</div>
  <ul class="facet country" style="top:78px">
    <li>Italy <em>(89)</em></li><li>France <em>(74)</em></li><li>Germany <em>(58)</em></li><li>Spain <em>(35)</em></li><li>South Africa <em>(14)</em></li><li>Austria <em>(12)</em></li><li>Australia <em>(12)</em></li><li>Portugal <em>(10)</em></li>
  </ul>
  <div class="scrolltrack"><i></i></div>

  <div class="facet-title" style="top:268px">TASTE</div>
  <ul class="facet" style="top:300px">
    <li>Dry <em>(303)</em></li><li>Half-dry <em>(8th)</em></li><li>Lovely <em>(6)</em></li><li>Sweet <em>(3)</em></li><li>Sweet <em>(1)</em></li>
  </ul>

  <div class="facet-title" style="top:432px">COLOR</div>
  <ul class="facet" style="top:464px">
    <li>red <em>(155)</em></li><li>White <em>(127)</em></li><li>Tingling <em>(23)</em></li><li>Rose <em>(13)</em></li><li>champagne <em>(9)</em></li>
  </ul>

  <div class="facet-title" style="top:592px">PRICE</div>
  <div class="slider"></div>
  <div class="price">2 € - 75 €</div>

  <div class="facet-title" style="top:672px">REGION</div>
  <div class="region">Region suchen ...</div>
</aside>

<section class="abs hero">
  <div class="hero-graphic" role="img" aria-label="Small nostalgic graphic of a single wine element, such as an old cork or grape, centred on white"></div>
  <div class="hero-title">Royal Quality Wine</div>
  <div class="hero-btn">Buy Now</div>
</section>

<div class="abs promo promo-ship">
  <p>FREE SHIPPING ON ORDER OVER</p>
  <div class="star">$25</div>
</div>
<div class="abs promo promo-ann">CELEBRATE YOUR<br>ANNIVERSARY WITH<br>TASTE</div>
<div class="abs promo promo-spec">SPECIALS<br>OFFER<b>20%<br>OFF</b></div>

<div class="abs section">
  <svg width="15" height="15" viewBox="0 0 15 15"><circle cx="7.5" cy="7.5" r="6.5" fill="none" stroke="#a8224a" stroke-width="1.3"/><path d="M6 4.5l3.5 3-3.5 3z" fill="#a8224a"/></svg>
  Selected Products
</div>
<div class="abs section-line"></div>
<div class="abs pager">
  <span><svg width="7" height="10"><path d="M6 1L2 5l4 4" fill="none" stroke="#333" stroke-width="1.3"/></svg></span>
  <span><svg width="7" height="10"><path d="M1 1l4 4-4 4" fill="none" stroke="#333" stroke-width="1.3"/></svg></span>
</div>

<div class="abs card" style="left:296px">
  <div class="bottle" role="img" aria-label="Bottle of rosé sparkling wine" style="background:linear-gradient(#d7c8cc,#e8a8b0 40%,#d98a96)"></div>
  <p>Rosato Brut, Colle Aurelia, Spumante</p>
</div>
<div class="abs card" style="left:498px">
  <div class="bottle" role="img" aria-label="Bottle of white wine" style="background:linear-gradient(#e8e8e8,#6b6b3e 25%,#4b4a2a)"></div>
  <p>Bianco del Lago Verde, Tenuta Morosa</p>
</div>
<div class="abs card" style="left:701px">
  <div class="bottle" role="img" aria-label="Bottle of red wine" style="background:linear-gradient(#1a1a1a,#2a2426 60%,#d9cfbd 60%,#d9cfbd 85%,#2a2426 85%)"></div>
  <p>Côte Rouge, AP, Domaine de Lavelle</p>
</div>
<div class="abs card" style="left:902px">
  <div class="bottle" role="img" aria-label="Bottle of amber dessert wine" style="background:linear-gradient(#2b2b3a,#b36a2a 35%,#e8dcc5 50%,#c57a34 90%)"></div>
  <p>Vino Ambrato Secco, Fenaroli</p>
</div>

</body>
</html>
```